Events & Entertainment Production Coordination Business Cards

We need a business card for a new company based in Los Angeles called "Bright Stage Works"
Our company brings people together for events and helps coordinate different productions. We bring artists from a different country to perform or do events in the U.S.
We are looking for something fun, lively, colorful, creative, and simple.
Nothing that looks too crisp, dark, stiff, or modern.
We connect people from different parts of the world, so definitely something eye-catching will be great!
Colors we would like to see are Black, Yellow, Red, White, Brown to name a few. (Feel free to use more!)
(Double-sided is an option also)
Industry/Entity Type
Business
Contact Information for Business Card
Contact Information to put on Business Card:
Name
Title
Address - 2 lines
Phone - place for 3 numbers
E-mail
URL
Look and feel

```html
<!DOCTYPE html>
<html lang="en">
<head>
<meta charset="utf-8">
<title>Bright Stage Works – Business Card</title>
<link href="https://fonts.googleapis.com/css2?family=Source+Sans+3:wght@400;600;700&display=swap" rel="stylesheet">
<style>
  :root {
    --stage-top: #2e2e2e;
    --stage-bottom: #040404;
    --card: #ffffff;
    --brand-brown: #b5470b;
    --brand-red: #e3120b;
    --ink: #111111;
  }
  * { box-sizing: border-box; margin: 0; padding: 0; }
  html, body { width: 1200px; height: 900px; overflow: hidden; }
  body {
    position: relative;
    background: linear-gradient(180deg, var(--stage-top) 0%, #1a1a1a 45%, var(--stage-bottom) 100%);
    font-family: "Source Sans 3", "Segoe UI", sans-serif;
    color: var(--ink);
  }
  .card {
    position: absolute;
    top: 306px;
    height: 271px;
    background: var(--card);
    border-radius: 10px;
    box-shadow: 0 2px 6px rgba(0,0,0,0.45);
  }
  .card--front { left: 149px; width: 439px; }
  .card--back { left: 608px; width: 441px; }

  .brand-mark {
    position: absolute;
    display: flex;
    flex-direction: column;
    align-items: center;
    color: var(--brand-brown);
    font-weight: 700;
  }
  .brand-mark__dot {
    border-radius: 50%;
    background: var(--brand-red);
  }
  .card--front .brand-mark { left: 44px; top: 62px; width: 160px; }
  .card--front .brand-mark__dot { width: 60px; height: 60px; margin-bottom: 16px; }
  .card--front .brand-mark__name { font-size: 18px; line-height: 1; white-space: nowrap; }

  .card--back .brand-mark { left: 0; right: 0; top: 44px; }
  .card--back .brand-mark__dot { width: 76px; height: 76px; margin-bottom: 34px; }
  .card--back .brand-mark__name { font-size: 38px; line-height: 1; white-space: nowrap; }

  .contact {
    position: absolute;
    left: 237px;
    top: 45px;
    font-size: 12.5px;
    line-height: 14px;
  }
  .contact__name {
    font-size: 17px;
    font-weight: 600;
    color: var(--brand-brown);
    line-height: 20px;
  }
  .contact__title { margin-bottom: 14px; }
  .contact__address { margin-bottom: 21px; }
  .contact__list { list-style: none; }
  .contact__item {
    display: flex;
    align-items: center;
    height: 18px;
  }
  .contact__icon {
    width: 9px;
    height: 9px;
    margin-right: 7px;
    fill: var(--brand-brown);
    flex: none;
  }
</style>
</head>
<body>
  <section class="card card--front">
    <div class="brand-mark">
      <span class="brand-mark__dot"></span>
      <span class="brand-mark__name">Bright Stage Works</span>
    </div>

    <div class="contact">
      <p class="contact__name">Daniel Reyes</p>
      <p class="contact__title">Managing Director</p>
      <p class="contact__address">12345, Address Goes Here<br>Country Name, 123456</p>
      <ul class="contact__list">
        <li class="contact__item">
          <svg class="contact__icon" viewBox="0 0 10 10"><path d="M2 0.5 L3.6 2.6 L2.8 3.6 Q4 6 6.4 7.2 L7.4 6.4 L9.5 8 L8.4 9.5 Q4.5 9.3 2 6.5 Q0.4 4.3 0.5 1.6 Z"/></svg>
          (044)-555-0190
        </li>
        <li class="contact__item">
          <svg class="contact__icon" viewBox="0 0 10 10"><path d="M2 0.5 L3.6 2.6 L2.8 3.6 Q4 6 6.4 7.2 L7.4 6.4 L9.5 8 L8.4 9.5 Q4.5 9.3 2 6.5 Q0.4 4.3 0.5 1.6 Z"/></svg>
          (044)-555-0191
        </li>
        <li class="contact__item">
          <svg class="contact__icon" viewBox="0 0 10 10"><path d="M2 0.5 L3.6 2.6 L2.8 3.6 Q4 6 6.4 7.2 L7.4 6.4 L9.5 8 L8.4 9.5 Q4.5 9.3 2 6.5 Q0.4 4.3 0.5 1.6 Z"/></svg>
          (044)-555-0192
        </li>
        <li class="contact__item">
          <svg class="contact__icon" viewBox="0 0 10 10"><path d="M0.5 2 H9.5 V8.5 H0.5 Z M0.5 2 L5 5.6 L9.5 2" stroke="#fff" stroke-width="0.8"/></svg>
          hello@brightstage.example
        </li>
        <li class="contact__item">
          <svg class="contact__icon" viewBox="0 0 10 10"><circle cx="5" cy="5" r="4.6"/><path d="M0.6 5 H9.4 M5 0.4 V9.6 M5 0.5 Q2.4 5 5 9.5 M5 0.5 Q7.6 5 5 9.5" stroke="#fff" stroke-width="0.7" fill="none"/></svg>
          www.brightstage.example
        </li>
      </ul>
    </div>
  </section>

  <section class="card card--back">
    <div class="brand-mark">
      <span class="brand-mark__dot"></span>
      <span class="brand-mark__name">Bright Stage Works</span>
    </div>
  </section>
</body>
</html>
```